Poster of Core Values & Motto

Create our core values poster and motto. Attached are our core values and our Motto. This poster represents both of our companies Tidy Pulp & CuraBinix.

Target Market(s)

Our team / employees

Industry/Entity Type

Shredding and Medical Waste

Colors
59FF00
82FF00
B8FF75
E3FFCB
F4FFEA
EB3D1F
EC4F4E
F09395
F8D3D4
FCEDEE

Requirements
Must have
• Include both companies logos

```html
<!DOCTYPE html>
<html lang="en">
<head>
<meta charset="utf-8">
<title>Purpose / Cause / Passion – Core Values Poster</title>
<link href="https://fonts.googleapis.com/css2?family=Oswald:wght@600;700&family=Yanone+Kaffeesatz:wght@400;500&display=swap" rel="stylesheet">
<style>
  :root {
    --backdrop: #dcdedd;
    --paper: #ffffff;
    --header-red: #d42027;
    --accent-lime: #82ff00;
    --slash-green: #7fd87f;
    --value-green: #00a94f;
    --value-orange: #e8401f;
    --heading-red: #d42027;
    --heading-dark: #1b4a33;
    --pink-band: #ee9496;
    --text-pale: #f4ffea;
    --icon-lime: #b8ff75;
    --logo-grey: #3a3a3a;
    --logo-green: #1f9a3c;
  }
  html, body {
    margin: 0;
    width: 1200px;
    height: 1179px;
    overflow: hidden;
    background: var(--backdrop);
  }
  .poster {
    display: block;
    width: 766px;
    height: 1179px;
    margin: 0 auto;
  }
  .title { font-family: "Oswald", sans-serif; font-weight: 600; fill: var(--paper); }
  .title-slash { fill: var(--slash-green); }
  .tagline { font-family: "Yanone Kaffeesatz", sans-serif; font-weight: 500; fill: var(--paper); }
  .value-heading {
    font-family: "Oswald", sans-serif;
    font-weight: 700;
    stroke: var(--paper);
    stroke-width: 5;
    paint-order: stroke;
  }
  .value-heading--red { fill: var(--heading-red); }
  .value-heading--dark { fill: var(--heading-dark); }
  .value-text { font-family: "Yanone Kaffeesatz", sans-serif; font-weight: 400; font-size: 34px; fill: var(--text-pale); }
  .band--green { fill: var(--value-green); }
  .band--orange { fill: var(--value-orange); }
  .pink { fill: var(--pink-band); }
  .icon-slot { fill: var(--icon-lime); opacity: 0.85; }
  .brand { font-family: "Yanone Kaffeesatz", sans-serif; font-weight: 500; font-size: 48px; }
  .brand--cura { fill: var(--logo-grey); }
  .brand--tidy { fill: var(--logo-green); }
</style>
</head>
<body>
<svg class="poster" viewBox="0 0 1117 1719" xmlns="http://www.w3.org/2000/svg" aria-label="Core values poster">
  <rect width="1117" height="1719" fill="var(--paper)"/>

  <!-- header -->
  <path d="M0 0 H1117 V332 C960 362 760 372 520 352 C320 335 140 312 0 318 Z" fill="var(--header-red)"/>
  <path d="M0 324 C140 318 320 341 520 358 C760 378 960 368 1117 336" fill="none" stroke="var(--accent-lime)" stroke-width="7"/>
  <text class="title" x="78" y="156" font-size="112" textLength="960" lengthAdjust="spacingAndGlyphs">PURPOSE <tspan class="title-slash">/</tspan> CAUSE <tspan class="title-slash">/</tspan> PASSION</text>
  <text class="tagline" x="133" y="259" font-size="54" textLength="850" lengthAdjust="spacingAndGlyphs">Remind people what great service looks like.</text>

  <!-- pink background accents -->
  <polygon class="pink" points="866,408 1117,408 1117,362 918,362"/>
  <polygon class="pink" points="900,760 1117,760 1117,578"/>
  <polygon class="pink" points="0,726 218,726 0,912"/>
  <polygon class="pink" points="863,1217 1117,1217 1117,1002"/>
  <polygon class="pink" points="0,1172 193,1172 0,1338"/>

  <!-- value bands -->
  <polygon class="band--green" points="379,400 750,400 427,676 56,676"/>
  <polygon class="band--orange" points="689,482 1060,482 737,759 366,759"/>
  <polygon class="band--green" points="379,808 750,808 427,1086 56,1086"/>
  <polygon class="band--orange" points="689,891 1060,891 737,1169 366,1169"/>
  <polygon class="band--green" points="379,1226 750,1226 427,1504 56,1504"/>
  <polygon class="band--orange" points="689,1310 1060,1310 737,1587 366,1587"/>

  <!-- icon slots -->
  <rect class="icon-slot" x="552" y="410" width="80" height="80" rx="12" role="img" aria-label="Team of people icon"/>
  <rect class="icon-slot" x="483" y="667" width="78" height="80" rx="12" role="img" aria-label="Trophy and person icon"/>
  <rect class="icon-slot" x="540" y="828" width="102" height="60" rx="12" role="img" aria-label="Armored money truck icon"/>
  <rect class="icon-slot" x="480" y="1078" width="72" height="76" rx="12" role="img" aria-label="Rocket and rising bar chart icon"/>
  <rect class="icon-slot" x="546" y="1238" width="80" height="82" rx="12" role="img" aria-label="Person with shield icon"/>
  <rect class="icon-slot" x="500" y="1480" width="88" height="90" rx="12" role="img" aria-label="Smiling worker with shield icon"/>

  <!-- values -->
  <text class="value-heading value-heading--red" x="175" y="459" font-size="88" textLength="310" lengthAdjust="spacingAndGlyphs">SYNERGY /</text>
  <text class="value-heading value-heading--red" x="175" y="544" font-size="88" textLength="352" lengthAdjust="spacingAndGlyphs">TEAMWORK</text>
  <text class="value-text" x="189" y="606">Get it done attitude with</text>
  <text class="value-text" x="189" y="642">humble confidence</text>

  <text class="value-heading value-heading--dark" x="647" y="609" font-size="88" textLength="338" lengthAdjust="spacingAndGlyphs">EXCELLENCE</text>
  <text class="value-text" x="618" y="654">Exceed expectations</text>
  <text class="value-text" x="618" y="690">with a smile</text>

  <text class="value-heading value-heading--red" x="212" y="862" font-size="88" textLength="283" lengthAdjust="spacingAndGlyphs">SAFE AND</text>
  <text class="value-heading value-heading--red" x="212" y="947" font-size="88" textLength="211" lengthAdjust="spacingAndGlyphs">SECURE</text>
  <text class="value-text" x="222" y="999">We are just as secure as</text>
  <text class="value-text" x="222" y="1035">an armored truck</text>
  <text class="value-text" x="222" y="1071">with money</text>

  <text class="value-heading value-heading--dark" x="758" y="989" font-size="88" textLength="272" lengthAdjust="spacingAndGlyphs">EFFICIENT</text>
  <text class="value-text" x="585" y="1026">On-time, sense of</text>
  <text class="value-text" x="585" y="1062">urgency, always trying</text>
  <text class="value-text" x="585" y="1098">to improve</text>

  <text class="value-heading value-heading--red" x="197" y="1284" font-size="88" textLength="308" lengthAdjust="spacingAndGlyphs">HONESTY /</text>
  <text class="value-heading value-heading--red" x="197" y="1368" font-size="88" textLength="303" lengthAdjust="spacingAndGlyphs">INTEGRITY</text>
  <text class="value-text" x="203" y="1434">Do the right thing</text>

  <text class="value-heading value-heading--dark" x="676" y="1409" font-size="88" textLength="359" lengthAdjust="spacingAndGlyphs">DEPENDABLE</text>
  <text class="value-text" x="682" y="1460">Do what you say</text>
  <text class="value-text" x="682" y="1496">you will do</text>

  <!-- company names -->
  <text class="brand brand--cura" x="510" y="1663">CuraBinix</text>
  <line x1="826" y1="1612" x2="826" y2="1700" stroke="#cfcfcf" stroke-width="2"/>
  <circle cx="885" cy="1648" r="18" fill="var(--logo-green)"/>
  <text class="brand brand--tidy" x="915" y="1663">Tidy Pulp</text>
</svg>
</body>
</html>
```